Pellmor Brochure

We need a brochure design for a new company based in Chicago called "Pellmor" We are a innovative On-Demand Cleaning company. web site and APP based ordering for Cleaning service. Our product is you need a Cleaner (Maid) we only use the term Cleaner we send one in the area to you for cleaning. All of our cleaners are professionals and certified and put through a third party security clearance check before entering your property.

Our company works like ZOLT.. we are truly On-Demand when you need us for home, small office and New Construction cleanings.

We work with relators, Condo associations, Apartment Complexes and Corporate apartment company's.

```html
<!DOCTYPE html>
<html lang="en">
<head>
<meta charset="utf-8">
<title>Pellmor Brochure</title>
<link rel="stylesheet" href="https://fonts.googleapis.com/css2?family=Arvo:wght@700&family=Open+Sans:wght@400;600&family=Ubuntu:wght@500;700&display=swap">
<style>
  :root {
    --green: #3aa83f;
    --green-dark: #2f9134;
    --teal: #1a9e92;
    --teal-dark: #15867c;
    --sand: #f4dcae;
    --sand-light: #fbf1de;
    --ink: #3e3a34;
    --stat-label: #4d4439;
    --paper: #ffffff;
    --backdrop: #e6e6e4;
  }
  * { margin: 0; padding: 0; box-sizing: border-box; }
  html, body { width: 1200px; height: 800px; overflow: hidden; }
  body { background: var(--backdrop); font-family: "Open Sans", Arial, sans-serif; color: var(--ink); }

  .spread {
    position: absolute; left: 50px; top: 40px;
    width: 1100px; height: 720px;
    display: flex; box-shadow: 0 6px 24px rgba(0,0,0,.18);
  }
  .page { position: relative; width: 550px; height: 720px; background: var(--paper); overflow: hidden; }

  .wave { position: absolute; left: 0; width: 100%; display: block; }

  /* Left page */
  .about-band {
    position: absolute; top: 0; left: 0; width: 100%; height: 62px;
    background: var(--green); display: flex; align-items: center; padding-left: 40px;
  }
  .about-band h2 { font-family: "Ubuntu", sans-serif; font-weight: 700; color: #fff; font-size: 24px; letter-spacing: .5px; }

  .company {
    position: absolute; top: 62px; left: 0; width: 100%; height: 300px;
    background: linear-gradient(180deg, var(--sand-light) 0%, var(--sand) 100%);
    padding: 42px 46px 0 50px;
  }
  .section-title { font-family: "Ubuntu", sans-serif; font-weight: 700; color: var(--green); font-size: 22px; margin-bottom: 6px; }
  .company p { font-size: 13px; line-height: 1.45; margin-bottom: 12px; }

  .values { position: absolute; top: 420px; left: 50px; right: 40px; }
  .values h3 { font-family: "Ubuntu", sans-serif; font-weight: 700; color: var(--green); font-size: 19px; line-height: 1.1; }
  .values p { font-size: 13px; line-height: 1.4; margin-bottom: 14px; }

  .stats {
    position: absolute; top: 540px; left: 0; width: 100%;
    display: flex; justify-content: space-around; padding: 0 30px;
  }
  .stat { text-align: center; }
  .stat-number { font-family: "Arvo", serif; font-weight: 700; color: var(--green); font-size: 50px; line-height: 1; }
  .stat-label { font-family: "Arvo", serif; font-weight: 700; color: var(--stat-label); font-size: 17px; }

  .green-foot { position: absolute; bottom: 0; left: 0; width: 100%; height: 56px; background: var(--green); }

  /* Right page */
  .service-band {
    position: absolute; top: 0; left: 0; width: 100%; height: 54px;
    background: var(--teal); display: flex; align-items: center; padding-left: 40px;
  }
  .service-band h2 { font-family: "Ubuntu", sans-serif; font-weight: 700; color: #fff; font-size: 24px; letter-spacing: .5px; }
  .service-sub { position: absolute; top: 58px; left: 40px; font-size: 12px; color: var(--ink); }

  .hero-photo {
    position: absolute; top: 80px; left: 0; width: 100%; height: 270px;
    background: linear-gradient(160deg, #f1f2f2 0%, #dcdedd 55%, #8f6d55 100%);
  }

  .tagline {
    position: absolute; top: 380px; left: 0; width: 100%; text-align: center;
    font-family: "Ubuntu", sans-serif; font-weight: 700; color: var(--teal); font-size: 26px; letter-spacing: .5px;
  }

  .price { position: absolute; top: 490px; left: 0; width: 100%; text-align: center; }
  .price-amount { font-family: "Arvo", serif; font-weight: 700; color: var(--teal); font-size: 54px; line-height: 1; }
  .price-label { font-family: "Arvo", serif; font-weight: 700; color: var(--stat-label); font-size: 18px; }

  .teal-foot {
    position: absolute; bottom: 0; left: 0; width: 100%; height: 76px;
    background: var(--teal); display: flex; align-items: center; justify-content: center;
  }
  .teal-foot a { font-family: "Arvo", serif; font-weight: 700; color: #fff; font-size: 24px; text-decoration: none; letter-spacing: .5px; }
</style>
</head>
<body>
<main class="spread">
  <section class="page page-about">
    <div class="company">
      <h3 class="section-title">Our company</h3>
      <p>Pellmor is the premier, next-generation cleaning company.</p>
      <p>We offer on-demand hourly cleaning services at the touch of a button, we're available 24/7 and our bonded, insured cleaners are the best in the business.</p>
      <p>Starting in Chicago, Pellmor is expanding to 13 cities nationwide, with collectively over 20 years of experience in the Service and Cleaning Industry.</p>
    </div>
    <svg class="wave" style="top:330px" width="550" height="60" viewBox="0 0 550 60" preserveAspectRatio="none">
      <path d="M0 30 C 90 0 180 60 280 32 C 380 4 460 50 550 20 L550 60 L0 60 Z" fill="#ffffff"/>
    </svg>
    <div class="about-band"><h2>About us</h2></div>

    <div class="values">
      <h3>Passion</h3>
      <p>Pellmor makes everything simple and clean.</p>
      <h3>Mission</h3>
      <p>To provide on-demand white glove cleaning services to complement your busy lifestyle. It's what you've been Pellmor for!</p>
    </div>

    <svg class="wave" style="top:520px" width="550" height="150" viewBox="0 0 550 150" preserveAspectRatio="none">
      <path d="M0 30 C 100 0 200 50 300 26 C 400 2 470 30 550 10 L550 150 L0 150 Z" fill="var(--sand)"/>
    </svg>
    <div class="stats">
      <div class="stat"><div class="stat-number">24</div><div class="stat-label">Hours a day</div></div>
      <div class="stat"><div class="stat-number">7</div><div class="stat-label">Days a Week</div></div>
      <div class="stat"><div class="stat-number">100</div><div class="stat-label">% Guaranteed</div></div>
    </div>
    <div class="green-foot"></div>
  </section>

  <section class="page page-service">
    <div class="service-band"><h2>On-Demand Cleaning 24/7</h2></div>
    <p class="service-sub">At a tap of a button your Home or Office can be cleaned in minutes.</p>
    <div class="hero-photo" role="img" aria-label="Photo of a cleaner vacuuming a bright modern living room floor"></div>
    <svg class="wave" style="top:330px" width="550" height="40" viewBox="0 0 550 40" preserveAspectRatio="none">
      <path d="M0 20 C 120 0 240 30 360 14 C 440 4 500 10 550 6 L550 40 L0 40 Z" fill="#ffffff"/>
    </svg>
    <p class="tagline">We tame the toughest messes!</p>

    <svg class="wave" style="top:445px" width="550" height="210" viewBox="0 0 550 210" preserveAspectRatio="none">
      <path d="M0 30 C 110 0 220 44 330 20 C 430 0 490 30 550 14 L550 210 L0 210 Z" fill="var(--sand)"/>
    </svg>
    <div class="price">
      <div class="price-amount">$40.00</div>
      <div class="price-label">Hourly Cleaning</div>
    </div>
    <div class="teal-foot"><a href="#">www.pellmor.com</a></div>
  </section>
</main>
</body>
</html>
```